Pelbrook Business Cards

Create new business cards with the details below.

Aaron Velst
Director

MB: +61 412 563 904
PH: 1300 417 639
Email: aaron.velst@pelbrook.com.au
Address: 27C Marlow Parade, Tarrowby NSW 2478 Australia
Website: www.pelbrook.com.au

Target Market(s)

Other business

Industry/Entity Type

Business

Requirements
Must have
• must be clean looking

```html
<!DOCTYPE html>
<html lang="en">
<head>
<meta charset="utf-8">
<title>Pelbrook Business Cards</title>
<link rel="stylesheet" href="https://fonts.googleapis.com/css2?family=Arimo:wght@400;700&display=swap">
<style>
  :root {
    --bg: #e6e6e6;
    --card: #ffffff;
    --lime: #8cc63f;
    --charcoal: #2b2b2b;
    --ink: #1e1e1e;
  }
  * { box-sizing: border-box; margin: 0; padding: 0; }
  html, body { width: 1200px; height: 1000px; overflow: hidden; }
  body {
    background: var(--bg);
    font-family: "Arimo", Arial, sans-serif;
    color: var(--ink);
    position: relative;
  }
  .card {
    position: absolute;
    left: 250px;
    width: 700px;
    height: 400px;
    background: var(--card);
    box-shadow: 0 6px 18px rgba(0,0,0,0.18);
    overflow: hidden;
  }
  /* Logo side */
  .card--brand { top: 70px; }
  .card--brand .edge-dark {
    position: absolute; left: 0; top: 0; bottom: 0; width: 12px;
    background: var(--charcoal);
  }
  .card--brand .edge-lime {
    position: absolute; left: 12px; top: 0; bottom: 0; width: 8px;
    background: var(--lime);
  }
  .brand {
    position: absolute; left: 0; right: 0; top: 0; bottom: 0;
    display: flex; align-items: center; justify-content: center; gap: 18px;
  }
  .brand__mark { width: 44px; height: 44px; background: var(--lime); }
  .brand__name {
    font-size: 64px; font-weight: 700; color: var(--charcoal); letter-spacing: 1px;
  }

  /* Contact side */
  .card--contact { top: 530px; }
  .band-top-dark { position: absolute; left: 0; right: 0; top: 0; height: 4px; background: var(--charcoal); }
  .band-top-lime { position: absolute; left: 0; right: 0; top: 4px; height: 8px; background: var(--lime); }
  .band-bottom-lime { position: absolute; left: 0; right: 0; bottom: 14px; height: 6px; background: var(--lime); }
  .band-bottom-dark { position: absolute; left: 0; right: 0; bottom: 0; height: 14px; background: var(--charcoal); }

  .person {
    position: absolute; right: 22px; top: 26px; text-align: right;
    font-size: 30px; line-height: 1.08;
  }
  .phones {
    position: absolute; left: 28px; top: 66px;
    font-size: 23px; line-height: 1.25;
  }
  .contacts {
    position: absolute; left: 16px; bottom: 30px;
    list-style: none; font-size: 19px;
  }
  .contacts li { display: flex; align-items: center; gap: 8px; height: 27px; }
  .contacts svg { width: 20px; height: 20px; flex: none; }
</style>
</head>
<body>

  <section class="card card--brand" aria-label="Business card front">
    <div class="edge-dark"></div>
    <div class="edge-lime"></div>
    <div class="brand">
      <span class="brand__mark"></span>
      <span class="brand__name">Pelbrook</span>
    </div>
  </section>

  <section class="card card--contact" aria-label="Business card back">
    <div class="band-top-dark"></div>
    <div class="band-top-lime"></div>

    <div class="person">
      <p class="person__name">Aaron Velst</p>
      <p class="person__title">Director</p>
    </div>

    <div class="phones">
      <p>MB: +61 412 563 904</p>
      <p>PH: 1300 417 639</p>
    </div>

    <ul class="contacts">
      <li>
        <svg viewBox="0 0 20 20" aria-hidden="true">
          <rect x="1" y="3" width="18" height="14" fill="var(--lime)"/>
          <path d="M1 3 L10 11 L19 3 M1 17 L8 9.5 M19 17 L12 9.5" stroke="#fff" stroke-width="1.6" fill="none"/>
        </svg>
        <span>aaron.velst@pelbrook.com.au</span>
      </li>
      <li>
        <svg viewBox="0 0 20 20" aria-hidden="true">
          <path d="M10 1 C5.5 1 3 4.3 3 7.5 C3 12 10 19 10 19 C10 19 17 12 17 7.5 C17 4.3 14.5 1 10 1 Z" fill="var(--lime)"/>
          <circle cx="10" cy="7.5" r="2.8" fill="#fff"/>
        </svg>
        <span>27C Marlow Parade, Tarrowby NSW 2478 Australia</span>
      </li>
      <li>
        <svg viewBox="0 0 20 20" aria-hidden="true">
          <circle cx="10" cy="10" r="9" fill="var(--lime)"/>
          <g stroke="#fff" stroke-width="1.2" fill="none">
            <ellipse cx="10" cy="10" rx="4" ry="8.5"/>
            <line x1="1.5" y1="10" x2="18.5" y2="10"/>
            <line x1="3" y1="5.5" x2="17" y2="5.5"/>
            <line x1="3" y1="14.5" x2="17" y2="14.5"/>
            <line x1="10" y1="1.5" x2="10" y2="18.5"/>
          </g>
        </svg>
        <span>www.pelbrook.com.au</span>
      </li>
    </ul>

    <div class="band-bottom-lime"></div>
    <div class="band-bottom-dark"></div>
  </section>

</body>
</html>
```